Modern Dental Appointment Reminder/Business Card

We already have a beautiful logo and icon picked from here on ArtisanHive, now we need someone to make them into a beautiful business card for us! This business card will also function as an appointment reminder card for patients. It will be double sided and must include:
Front
-Contact Info as Follows:
(Gavin R Moss, DDS
Family and Cosmetic Dentistry
2946 S 1320 E Ste 400
Millbrook, Oregon 84137)
-Our Logo or Icon (your choice, if Icon must write "Bellmere Dental" below it like in the example file)
Back
-"You're Invited!"
-"Your next appointment is on"
-Place to write date & time
-"Please call 24hrs ahead if appointment is to be cancelled
-Our Icon

Logo and Icon to be used are attached below, along with an example of what we need.
Please do NOT use lots of red! We want the red to just be an accent. Please use grey, white, or even a muted teal for the majority of the card.

Industry/Entity Type

Dentistry

Contact Information for Business Card

Gavin R Moss, DDS
2946 S 1320 E Ste 400
Millbrook, Oregon 84137

Colors
cfeae6

Requirements
Should not have
• Lots of red!

```html
<!DOCTYPE html>
<html lang="en">
<head>
<meta charset="utf-8">
<title>Bellmere Dental – Business &amp; Appointment Card</title>
<link href="https://fonts.googleapis.com/css2?family=Jost:wght@400;500;700&family=Yellowtail&display=swap" rel="stylesheet">
<style>
  :root {
    --page: #e9e7e4;
    --taupe: #5d554c;
    --white: #ffffff;
    --accent-red: #a8231f;
    --mint: #cfeae6;
    --ink: #4a433b;
  }
  * { box-sizing: border-box; margin: 0; padding: 0; }
  html, body {
    width: 1200px; height: 970px; overflow: hidden;
    background: var(--page);
    font-family: "Jost", sans-serif;
  }
  .card {
    position: absolute;
    width: 760px; height: 434px;
    overflow: hidden;
    box-shadow: 0 10px 24px rgba(0,0,0,.18);
  }

  /* ---------- Front ---------- */
  .card--front { left: 110px; top: 34px; background: var(--taupe); }
  .front-sweep { position: absolute; inset: 0; }
  .brand-mark {
    position: absolute; left: 470px; top: 86px;
    width: 180px; height: 180px; border-radius: 50%;
    background: var(--taupe);
    display: flex; align-items: center; justify-content: center;
  }
  .brand-mark__inner {
    width: 150px; height: 150px; border-radius: 50%;
    background: var(--white);
    display: flex; align-items: center; justify-content: center;
    text-align: center;
    color: var(--taupe); font-weight: 500; font-size: 22px; line-height: 1.1;
  }
  .contact { position: absolute; left: 60px; top: 242px; color: var(--white); }
  .contact__title {
    font-weight: 700; font-size: 21px; display: inline-block;
    padding-bottom: 3px; border-bottom: 3px solid var(--accent-red);
    margin-bottom: 8px;
  }
  .contact__line { font-size: 22px; line-height: 1.3; font-weight: 400; letter-spacing: .3px; }

  /* ---------- Back ---------- */
  .card--back { left: 330px; top: 500px; background: var(--taupe); color: var(--white); }
  .back-mark {
    position: absolute; left: 330px; top: 36px;
    width: 120px; height: 120px; border-radius: 50%;
    background: var(--white);
    display: flex; align-items: center; justify-content: center; text-align: center;
    color: var(--taupe); font-weight: 500; font-size: 17px; line-height: 1.1;
  }
  .back-address {
    position: absolute; left: 480px; top: 46px;
    font-size: 18px; line-height: 1.4;
  }
  .invite { position: absolute; left: 50px; top: 148px; }
  .invite__title { font-family: "Yellowtail", cursive; font-size: 44px; line-height: 1; }
  .invite__sub { font-size: 15px; margin-top: 6px; letter-spacing: .3px; }
  .slot { position: absolute; left: 70px; display: flex; align-items: flex-end; width: 610px; }
  .slot--date { top: 236px; }
  .slot--time { top: 272px; left: 92px; width: 588px; }
  .slot__label { font-size: 19px; width: 68px; }
  .slot__line { flex: 1; border-bottom: 2px dotted var(--white); margin-bottom: 6px; }
  .phones {
    position: absolute; left: 200px; top: 302px;
    font-size: 20px; letter-spacing: .5px; display: flex; gap: 48px;
  }
  .notice {
    position: absolute; left: 0; right: 0; top: 346px; height: 54px;
    background: var(--mint); color: var(--ink);
    display: flex; align-items: center; justify-content: center;
    font-size: 21px; font-weight: 500; letter-spacing: .3px;
  }
</style>
</head>
<body>

<section class="card card--front" aria-label="Business card front">
  <svg class="front-sweep" viewBox="0 0 760 434" width="760" height="434" aria-hidden="true">
    <path d="M0 0 H760 V150 C560 160 300 186 0 222 Z" fill="var(--white)"/>
    <path d="M160 200 C330 180 520 160 760 140 L760 150 C520 170 330 188 160 203 Z" fill="var(--accent-red)"/>
  </svg>
  <div class="brand-mark">
    <div class="brand-mark__inner">Bellmere<br>Dental</div>
  </div>
  <div class="contact">
    <div class="contact__title">Contact Info</div>
    <p class="contact__line">Gavin R Moss, DDS.</p>
    <p class="contact__line">Family and Cosmetic Dentistry.</p>
    <p class="contact__line">2946 S 1320 E Ste 400</p>
    <p class="contact__line">Millbrook, Oregon 84137</p>
  </div>
</section>

<section class="card card--back" aria-label="Appointment card back">
  <div class="back-mark">Bellmere<br>Dental</div>
  <div class="back-address">
    <p>2946 S 1320 E Ste 400</p>
    <p>Millbrook, Oregon 84137</p>
  </div>
  <div class="invite">
    <p class="invite__title">You're Invited!</p>
    <p class="invite__sub">Your next appointment is on</p>
  </div>
  <div class="slot slot--date"><span class="slot__label">Date</span><span class="slot__line"></span></div>
  <div class="slot slot--time"><span class="slot__label">Time</span><span class="slot__line"></span></div>
  <div class="phones">
    <span>P : 801.555.0142</span>
    <span>F : 801.555.0178</span>
  </div>
  <div class="notice">Please call 24hrs ahead if appointment is to be cancelled</div>
</section>

</body>
</html>
```